Welding and farication business card

Business name Tbm Welding & Fabrication

I need a business card made for my welding and fabrication business that is bold and stands out. My business is both welding repairs on machinery and anything else you can imagine as well as fabricating new products. i have used this service before and was very happy with the out come of my design logo. i think the card should remain fairly simple and classy but also be bold. I think a black card would best be suited to the talk with my logo on it. i feel the back of the card should just have my logo and the front have my logo email, website and phone number and maybe incorporate a facebook and instagram simple if it can be made look good these arnt a necessity.
I have included both my logo and some business card ideas below

Target Market(s)

Farmers, heavy industry, earthmoving, trucking

Industry/Entity Type

Engineering

Contact Information for Business Card

0438517264
dale@tbmweldingandfabrication.com.au
www.tbmweldingandfabrication.com.au

Colors
33a6d7
0255a3

Requirements
Must have
• Dale Hutchins
my phone number 0438517264
my logo
Preferably a black card desgn
Nice to have
• List of what i do,
Sheds and carports
Ute trays
Stockyards
Trailers
Farm equipment
Stockcrates
Gateways and Entrances
Breakdowns
Maintenance
And lots more!

```html
<!DOCTYPE html>
<html lang="en">
<head>
<meta charset="UTF-8">
<title>Tbm Welding &amp; Fabrication – Business Card Back</title>
<link rel="stylesheet" href="https://fonts.googleapis.com/css2?family=Saira+Semi+Condensed:wght@700&display=swap">
<style>
  :root {
    --card-black: #060707;
    --ink-white: #ffffff;
    --accent-blue: #1f4fd1;
  }
  html, body {
    margin: 0;
    padding: 0;
    width: 1200px;
    height: 686px;
    overflow: hidden;
    background: var(--card-black);
  }
  .card {
    position: relative;
    width: 1200px;
    height: 686px;
    background: var(--card-black);
    overflow: hidden;
  }
  .brand-name {
    position: absolute;
    left: 0;
    right: 0;
    top: 300px;
    margin: 0;
    text-align: center;
    font-family: "Saira Semi Condensed", "Arial Narrow", sans-serif;
    font-weight: 700;
    font-size: 44px;
    letter-spacing: 1px;
    color: var(--ink-white);
    line-height: 1;
  }
  .wave {
    position: absolute;
    left: 0;
    top: 0;
    width: 1200px;
    height: 686px;
  }
  .wave-blue { fill: var(--accent-blue); }
  .wave-white { fill: var(--ink-white); }
</style>
</head>
<body>
  <main class="card">
    <h1 class="brand-name">Tbm Welding &amp; Fabrication</h1>
    <svg class="wave" viewBox="0 0 1200 686" aria-hidden="true">
      <path class="wave-blue"
        d="M11,594 C70,620 130,636 200,636 C340,634 460,598 620,552 C780,506 900,468 1000,466 C1090,465 1150,515 1200,562
           L1200,572 C1140,530 1070,486 990,484 C880,484 760,530 610,576 C460,622 330,646 200,644 C120,642 60,622 11,594 Z"/>
      <path class="wave-white"
        d="M11,594 C70,620 130,636 200,636 C340,634 460,598 620,552 C780,506 900,468 1000,466 C1040,466 1075,474 1105,487
           C1070,479 1030,475 990,475 C880,476 760,520 610,566 C460,612 330,640 200,640 C120,639 60,620 11,594 Z"/>
    </svg>
  </main>
</body>
</html>
```